New Organic Skin Care Line Needs to Design a Product Label

***THE WINNER OF THIS PROJECT WILL MOST LIKELY BECOME THE EXCLUSIVE DESIGNER FOR OUR OTHER PRODUCT LABELS***

We need a label design for a new organic skin care product line called "Maple Dune Festoon." This specific product is a 100% pure organic coconut oil. It's used for skin hydration, protection, and makeup removal.

Info to include on front label:

1. Logo: Maple Dune Festoon (attached)
2. Product Name: Pure Coconut Oil (emphasize "organic" somewhere)
3. Slogan: Hydrate your skin and hair.
4. Size: 8 FL OZ 236mL

Attached is:

1. The brand logo "Maple Dune Festoon" with a white background.
2. An image of the bottle we will use.
3. An image of the bottle with lines to show the size and placement of the label.
4. The brand logo "Maple Dune Festoon" with a black background. (photoshop file)

What we need:

A simple mock up of the front side of the label on the bottle. We first want to know what it will look like on the bottle given the size and dimensions.

- We would like one label with a white background (including the logo with a white background).
- We would like a second label with a black background (including the logo with a black background, just need to make the black font white instead of black).

We can get a great idea of what to expect from the front side of the label so we will complete the back side once we identify a winner.
Updates

Apologies, but we are now using a different bottle. The previous one is now discontinued. Please view the two most recent images uploaded. One is an image of the new bottle by itself. The other is an image of that bottle with instructions. Please use your most recent designs on the new bottle. Feel free to make any modifications you see fit to compliment the new bottle shape. Added Friday, March 18, 2016

Project Deadline Extended
Reason: We are still working with the label company to finalize the size. Once the size is confirmed we will have to tweak labels based on finalized measurements.

Target Market(s)

Women, 18-70

Industry/Entity Type

Skin Care Product

Font styles to use
Decorative
Script

Requirements
Must have
• -"shabby sheek" and "cute" theme
• -soft organic feel
• -the ingredients are organic, pure, and natural. That should be an essence of the label.

```html
<!DOCTYPE html>
<html lang="en">
<head>
<meta charset="UTF-8">
<title>Maple Dune Festoon – Organic Pure Coconut Oil Label</title>
<link rel="stylesheet" href="https://fonts.googleapis.com/css2?family=Marck+Script&family=Pinyon+Script&family=Libre+Baskerville&display=swap">
<style>
  :root {
    --page-bg: #f4f4f5;
    --label-white: #fbfdfe;
    --wash-light: #dcf0f7;
    --wash-mid: #b6e1ef;
    --wash-deep: #9dd4e8;
    --ink-dark: #1c1a1b;
    --ink-grey: #8a8f93;
    --brand-ink: #4a4c50;
    --brand-accent: #c2397a;
  }
  * { margin: 0; padding: 0; box-sizing: border-box; }
  html, body {
    width: 1200px;
    height: 1200px;
    overflow: hidden;
    background: var(--page-bg);
  }
  .canvas {
    position: relative;
    width: 1200px;
    height: 1200px;
  }
  .label {
    position: absolute;
    left: 150px;
    top: 190px;
    width: 900px;
    height: 810px;
  }
  .label-shape {
    position: absolute;
    inset: 0;
    width: 100%;
    height: 100%;
  }
  .label-content {
    position: absolute;
    inset: 0;
    display: flex;
    flex-direction: column;
    align-items: center;
    text-align: center;
    padding-top: 160px;
  }
  .brand {
    display: flex;
    align-items: center;
    gap: 12px;
    font-family: "Libre Baskerville", serif;
    font-size: 26px;
    letter-spacing: 3px;
    text-transform: uppercase;
    color: var(--brand-ink);
  }
  .brand-dot {
    width: 12px;
    height: 12px;
    border-radius: 50%;
    background: var(--brand-accent);
  }
  .product-claim {
    margin-top: 6px;
    font-family: "Marck Script", cursive;
    font-size: 138px;
    line-height: 1.05;
    color: var(--ink-dark);
  }
  .product-name {
    margin-top: 4px;
    font-family: "Pinyon Script", cursive;
    font-size: 44px;
    color: var(--ink-grey);
  }
  .slogan {
    margin-top: 30px;
    font-family: "Libre Baskerville", serif;
    font-size: 25px;
    letter-spacing: 1px;
    color: var(--ink-grey);
  }
  .size {
    margin-top: 30px;
    font-family: "Libre Baskerville", serif;
    font-size: 20px;
    letter-spacing: 1px;
    color: var(--ink-grey);
  }
</style>
</head>
<body>
<main class="canvas">
  <section class="label">
    <svg class="label-shape" viewBox="0 0 1000 900" preserveAspectRatio="none" role="img" aria-label="Heart-shaped label with a soft pale blue watercolor wash">
      <defs>
        <linearGradient id="wash-base" x1="0" y1="0" x2="0" y2="1">
          <stop offset="0" stop-color="var(--label-white)"/>
          <stop offset="0.45" stop-color="var(--wash-light)"/>
          <stop offset="1" stop-color="var(--wash-mid)"/>
        </linearGradient>
        <radialGradient id="wash-left" cx="0.2" cy="0.25" r="0.35">
          <stop offset="0" stop-color="var(--wash-deep)" stop-opacity="0.55"/>
          <stop offset="1" stop-color="var(--wash-deep)" stop-opacity="0"/>
        </radialGradient>
        <radialGradient id="wash-right" cx="0.8" cy="0.55" r="0.35">
          <stop offset="0" stop-color="var(--wash-deep)" stop-opacity="0.6"/>
          <stop offset="1" stop-color="var(--wash-deep)" stop-opacity="0"/>
        </radialGradient>
        <radialGradient id="wash-bottom" cx="0.45" cy="0.85" r="0.3">
          <stop offset="0" stop-color="var(--wash-deep)" stop-opacity="0.7"/>
          <stop offset="1" stop-color="var(--wash-deep)" stop-opacity="0"/>
        </radialGradient>
        <clipPath id="heart-clip">
          <path d="M500 885 L115 470 C15 360 35 165 190 105 C320 55 440 125 500 225 C560 125 680 55 810 105 C965 165 985 360 885 470 Z"/>
        </clipPath>
      </defs>
      <g clip-path="url(#heart-clip)">
        <rect width="1000" height="900" fill="url(#wash-base)"/>
        <rect width="1000" height="900" fill="url(#wash-left)"/>
        <rect width="1000" height="900" fill="url(#wash-right)"/>
        <rect width="1000" height="900" fill="url(#wash-bottom)"/>
      </g>
    </svg>
    <div class="label-content">
      <div class="brand"><span class="brand-dot"></span>Maple Dune Festoon</div>
      <h1 class="product-claim">Organic</h1>
      <p class="product-name">Pure Coconut Oil</p>
      <p class="slogan">Hydrate your skin and hair</p>
      <p class="size">8 FL OZ 236mL</p>
    </div>
  </section>
</main>
</body>
</html>
```